Business Card Design

​Silver Harbor Rhythms provides personal, friendly service in a fun and high energy environment. We are based in Vermont.

We would like a card that appeals to a wide range of audiences as we do a wide range of events. Please feel free to check out our website silverharborrhythms.com for inspiration.

Target Market(s)

weddings, corporate, birthday parties, colleges

Industry/Entity Type

Business

Contact Information for Business Card

Silver Harbor Rhythms
Providing Entertainment For All Occasions
555 014 2968
silverharborrhythms@mailquill.net
silverharborrhythms.com

```html
<!DOCTYPE html>
<html lang="en">
<head>
<meta charset="utf-8">
<title>Silver Harbor Rhythms – Business Card</title>
<link href="https://fonts.googleapis.com/css2?family=Roboto+Condensed:wght@500&display=swap" rel="stylesheet">
<style>
  :root {
    --green: #0b5a2e;
    --red: #c0282a;
    --red-dark: #6e1416;
    --white: #ffffff;
  }
  html, body {
    margin: 0;
    padding: 0;
    overflow: hidden;
    background: var(--white);
  }
  .card {
    position: relative;
    width: 1200px;
    height: 702px;
    overflow: hidden;
    background: var(--white);
    font-family: "Roboto Condensed", "Arial Narrow", sans-serif;
    font-weight: 500;
  }
  .wave-area {
    position: absolute;
    left: 0;
    top: 455px;
    width: 1200px;
    height: 247px;
    background: linear-gradient(90deg, var(--red-dark) 0%, var(--red) 22%, var(--green) 50%, var(--green) 100%);
  }
  .brand-name {
    position: absolute;
    left: 72px;
    top: 300px;
    width: 620px;
    margin: 0;
    color: var(--green);
    font-size: 56px;
    line-height: 1;
    font-weight: 500;
    white-space: nowrap;
    display: flex;
    align-items: center;
    justify-content: center;
    gap: 16px;
  }
  .brand-mark {
    width: 24px;
    height: 24px;
    border-radius: 50%;
    background: var(--red);
    flex: none;
  }
  .tagline {
    position: absolute;
    right: 51px;
    top: 80px;
    margin: 0;
    text-align: right;
    color: var(--green);
    font-size: 34px;
    line-height: 59px;
  }
  .contacts {
    position: absolute;
    right: 52px;
    top: 480px;
    margin: 0;
    padding: 0;
    list-style: none;
    color: var(--white);
    font-size: 31px;
  }
  .contacts li {
    display: flex;
    align-items: center;
    justify-content: flex-end;
    gap: 18px;
    height: 55px;
  }
  .contacts svg {
    width: 36px;
    height: 30px;
    flex: none;
  }
</style>
</head>
<body>
<div class="card">
  <div class="wave-area" role="img" aria-label="Decorative red and green wave band across the bottom of the card"></div>

  <h1 class="brand-name"><span class="brand-mark"></span>Silver Harbor Rhythms</h1>

  <p class="tagline">Silver Harbor Rhythms<br>Providing Entertainment<br>For All Occasions</p>

  <ul class="contacts">
    <li>555 014 2968
      <svg viewBox="0 0 36 30" aria-hidden="true">
        <path fill="var(--white)" d="M3,9 C3,3 33,3 33,9 L33,12 L26,12 L26,8 L10,8 L10,12 L3,12 Z"/>
        <path fill="var(--white)" d="M11,11 L25,11 L31,26 L5,26 Z"/>
        <circle cx="18" cy="19" r="4" fill="var(--green)"/>
      </svg>
    </li>
    <li>silverharborrhythms.com
      <svg viewBox="0 0 36 30" aria-hidden="true">
        <g fill="none" stroke="var(--white)" stroke-width="2">
          <circle cx="18" cy="15" r="12"/>
          <ellipse cx="18" cy="15" rx="5" ry="12"/>
          <line x1="6" y1="15" x2="30" y2="15"/>
          <path d="M8,9 H28 M8,21 H28"/>
        </g>
      </svg>
    </li>
    <li>silverharborrhythms@mailquill.net
      <svg viewBox="0 0 36 30" aria-hidden="true">
        <g fill="none" stroke="var(--white)" stroke-width="2">
          <rect x="3" y="6" width="30" height="19"/>
          <path d="M3,6 L18,18 L33,6 M3,25 L14,15 M33,25 L22,15"/>
        </g>
      </svg>
    </li>
  </ul>
</div>
</body>
</html>
```